Plastic Surgeon Needs a business card desing

I need a plastic surgeon business card, Im young , innovative , not afraid of thinking out of the box, What I dont like is human figures or scalpes as designing the card, because I think they are old fashion, I think my name is my strongest card, so I try to find the desing to be something elegant , simple , slick , stylish , radiant with carimsa!

Target Market(s)

PLastics Surgery Patients and doctors to have my data

Industry/Entity Type

Plastic

Contact Information for Business Card

phone numbers need to be legible , right now i have grey scales so they a not to legible

Font styles to use
Serif
Sans Serif

Requirements
Must have
• Personality, and it has to look like a doctor card, not a buisness man card, that is why i think it should be clean , clear , and legible
Nice to have
• Stylilsh, not to heavy card, in means of colors and logos, i think it should give a sensation of health
• Im not sure to have the logo of the hospital i work
Should not have
• human figures
• Hands
• Surgeons

```html
<!DOCTYPE html>
<html lang="es">
<head>
<meta charset="utf-8">
<title>Dr. Marco Velarde – Tarjetas de presentación</title>
<link rel="stylesheet" href="https://fonts.googleapis.com/css2?family=Arimo:wght@400;700&display=swap">
<style>
  :root {
    --page: #e9e7e3;
    --ink: #0c0c0c;
    --ink-soft: #2a2a2a;
    --paper: #f7f7f5;
    --paper-shade: #e4e4e2;
    --white: #ffffff;
    --text-dark: #1d1d1d;
  }
  * { margin: 0; padding: 0; box-sizing: border-box; }
  html, body {
    width: 1200px; height: 902px; overflow: hidden;
    background: var(--page);
    font-family: "Arimo", Arial, sans-serif;
  }
  .canvas { position: relative; width: 1200px; height: 902px; }

  .card {
    position: absolute;
    width: 560px; height: 320px;
    border-radius: 4px;
    box-shadow: 0 10px 28px rgba(0,0,0,.22);
    overflow: hidden;
  }

  /* Front */
  .card--front {
    left: 70px; top: 70px;
    background: linear-gradient(135deg, #2b2b2b 0%, var(--ink) 45%, #050505 100%);
    color: var(--white);
  }
  .card--front .identity { position: absolute; left: 44px; top: 92px; }
  .name {
    font-size: 30px; font-weight: 400; letter-spacing: .5px;
    text-transform: uppercase; line-height: 1; white-space: nowrap;
  }
  .specialty { font-size: 16px; margin-top: 6px; letter-spacing: .2px; white-space: nowrap; }
  .brand {
    position: absolute; right: 52px; top: 196px;
    display: flex; align-items: center; gap: 14px;
    font-size: 22px; font-weight: 400; letter-spacing: 3px;
    color: var(--white);
  }
  .brand__dot { width: 34px; height: 34px; border-radius: 50%; background: var(--white); flex: none; }

  /* Back */
  .card--back {
    left: 570px; top: 510px;
    background: linear-gradient(160deg, var(--white) 0%, var(--paper) 60%, var(--paper-shade) 100%);
    color: var(--text-dark);
  }
  .band-rule { position: absolute; left: 0; right: 0; height: 2px; background: var(--ink); }
  .band-rule--top { top: 36px; }
  .band-rule--bottom { top: 152px; }
  .band {
    position: absolute; left: 0; right: 0; top: 42px; height: 104px;
    background: linear-gradient(90deg, var(--ink-soft) 0%, var(--ink) 50%, #111 100%);
    color: var(--white);
  }
  .band::before, .band::after {
    content: ""; position: absolute; left: 0; right: 0; height: 1px; background: var(--white);
  }
  .band::before { top: 5px; }
  .band::after { bottom: 5px; }
  .band .identity { position: absolute; left: 38px; top: 24px; }
  .contact {
    position: absolute; left: 250px; right: 30px; top: 172px;
    text-align: center; font-size: 14px; line-height: 1.45;
    font-style: normal;
  }
  .contact .address { margin-bottom: 6px; }
  .contact p { margin: 0; }
</style>
</head>
<body>
<main class="canvas">

  <section class="card card--front" aria-label="Frente de la tarjeta">
    <div class="identity">
      <h1 class="name">Dr. Marco Velarde</h1>
      <p class="specialty">Cirugia plastica, estetica y reconstructiva</p>
    </div>
    <div class="brand"><span class="brand__dot"></span><span>VELARDE</span></div>
  </section>

  <section class="card card--back" aria-label="Reverso de la tarjeta">
    <div class="band-rule band-rule--top"></div>
    <div class="band">
      <div class="identity">
        <h2 class="name">Dr. Marco Velarde</h2>
        <p class="specialty">Cirugia plastica, estetica y reconstructiva</p>
      </div>
    </div>
    <div class="band-rule band-rule--bottom"></div>

    <address class="contact">
      <div class="address">
        <p>Av. Olivos 1820, Int. 45</p>
        <p>Torre Médica Alameda</p>
        <p>Zapopan, Jalisco, Mexico</p>
      </div>
      <p>P : 01 (33) 3512 7740</p>
      <p>C : 33 3261 5082</p>
      <p>E : marco@drvelarde.com</p>
    </address>
  </section>

</main>
</body>
</html>
```